Hotel Business Card Project

Amber Crest Hotel will be a premium boutique hotel in Dhaka, Bangladesh. The hotel will offer the finest amenities and facilities available on the market, and the cost per room investment will far exceed other 5-star hotels currently in the market.

As a result, we wanted the business card to reflect that premium/luxurious/upscale feel, and also be elegant and hospitable at the same time.

The name 'Amber Crest' is derived from the fact that Bangladesh has 6 distinct seasons (you can get more information online if required, or contact me about it). The leaves in the logo has the tree because trees give people shade, protection and safety (just like our hotel would try to give).

Target Market(s)

Business professionals, guests

Industry/Entity Type

Investment

Requirements
Must have
• Elegant, Classy and very attractive business card.

Must be editable to enter specific Names, Positions, Phone numbers and email later on.
Nice to have
• The address would be: House 47, Road 23, Lakeview 5, Dhaka 1208, Bangladesh

Slogan- Luxury Redefined

```html
<!DOCTYPE html>
<html lang="en">
<head>
<meta charset="utf-8">
<title>Amber Crest Hotel – Business Card</title>
<link href="https://fonts.googleapis.com/css2?family=Open+Sans:wght@400&display=swap" rel="stylesheet">
<style>
  :root {
    --backdrop: #6d6e70;
    --card-white: #ffffff;
    --card-edge: #eeeeee;
    --band-tan: #c8b592;
    --band-rule: #ece7dd;
    --band-text: #ffffff;
    --brand-grey: #6f6f6f;
    --mark-amber: #d9a25a;
    --name-grey: #6a6a6a;
    --position-grey: #bdbdbd;
  }
  * { margin: 0; padding: 0; box-sizing: border-box; }
  html, body {
    width: 1200px;
    height: 451px;
    overflow: hidden;
    background: var(--backdrop);
    font-family: "Open Sans", Arial, sans-serif;
  }
  .canvas { position: relative; width: 1200px; height: 451px; }

  .card {
    position: absolute;
    width: 518px;
    height: 299px;
    background: radial-gradient(ellipse at 50% 40%, var(--card-white) 40%, var(--card-edge) 100%);
    overflow: hidden;
  }
  .card--front { left: 72px; top: 60px; }
  .card--back  { left: 617px; top: 64px; }

  .band {
    position: absolute;
    left: 0; right: 0; bottom: 0;
    background: var(--band-tan);
    border-top: 7px solid var(--band-rule);
    color: var(--band-text);
  }
  .card--front .band { height: 46px; }
  .card--back .band { height: 100px; }

  .brand {
    position: absolute;
    display: flex;
    flex-direction: column;
    align-items: center;
    color: var(--brand-grey);
  }
  .brand__mark {
    border-radius: 50%;
    background: var(--mark-amber);
  }
  .brand__name {
    text-transform: uppercase;
    letter-spacing: 0.04em;
    white-space: nowrap;
  }
  .brand__sub {
    text-transform: uppercase;
    letter-spacing: 0.2em;
  }

  .card--front .brand { left: 0; right: 0; top: 40px; }
  .card--front .brand__mark { width: 96px; height: 96px; margin-bottom: 18px; }
  .card--front .brand__name { font-size: 34px; line-height: 40px; }
  .card--front .brand__sub { font-size: 12px; line-height: 14px; }

  .tagline {
    text-align: center;
    font-size: 22px;
    line-height: 39px;
  }

  .card--back .brand { left: 28px; width: 172px; top: 16px; }
  .card--back .brand__mark { width: 74px; height: 74px; margin-bottom: 14px; }
  .card--back .brand__name { font-size: 22px; line-height: 26px; }
  .card--back .brand__sub { font-size: 9px; line-height: 11px; }

  .person { position: absolute; left: 294px; top: 54px; }
  .person__name { font-size: 26px; line-height: 32px; color: var(--name-grey); }
  .person__position { font-size: 18px; line-height: 22px; color: var(--position-grey); }

  .address {
    position: absolute;
    left: 31px; top: 12px;
    font-size: 18px;
    line-height: 24px;
    font-style: normal;
    width: 240px;
  }
  .contact {
    position: absolute;
    left: 294px; top: 36px;
    font-size: 20px;
    line-height: 26px;
  }
</style>
</head>
<body>
<main class="canvas">
  <section class="card card--front">
    <div class="brand">
      <span class="brand__mark"></span>
      <span class="brand__name">Amber Crest</span>
      <span class="brand__sub">Hotel</span>
    </div>
    <div class="band">
      <p class="tagline">Luxury Redefined</p>
    </div>
  </section>

  <section class="card card--back">
    <div class="brand">
      <span class="brand__mark"></span>
      <span class="brand__name">Amber Crest</span>
      <span class="brand__sub">Hotel</span>
    </div>
    <div class="person">
      <p class="person__name">Names</p>
      <p class="person__position">Positions</p>
    </div>
    <div class="band">
      <address class="address">House 47, Road 23, Lakeview 5, Dhaka 1208, Bangladesh</address>
      <div class="contact">
        <p>Phone numbers</p>
        <p>email</p>
      </div>
    </div>
  </section>
</main>
</body>
</html>
```